Starter & Alternator business needs a website

update: very good designs submitted so far. also need this to display well on mobile devices. not sure if wordpress or html/css is better for my needs.

Our existing website is vexlandrib.com and is need of total revamp. Need full design of a website for my business.

We sell and rebuild starters and alternators. Customers bring in the units and we rebuild them. Or we sell them brand new or rebuilt units we have in stock. We do not install units into vehicles like a mechanic would. We strictly rebuild starters and alternators in our shop, sell brand new units over the counter, and we do deliver occasionally as well. We do offer a line of Morlin batteries as well but that is only a small feature of the business.

I would like this website designed and coded. I can upload the files to my web host after completion. I can also add in and modify content like our background info, etc.

I have included an illustrator file that shows some of our signage and logo, etc. I have also included a radio commercial sample so you can get a little better feel for the business. A similar ad does run on the radio currently, slightly different and without the added sound effects.

Update: I do like using photos of real items(starters or alternators etc) for an icon, like a real alternator stock image for the alternator section icon, etc. Maybe incorporate our logo in that design as well. That looks nice as well and may aid in navigation.

For any other design elements, do what you think looks good. Our colors are red/white/blue as seen in the illustrator file. our building is painted with talbot greaves colors, emberglow red and deep harbor for blue.

Here are some examples of rebuilders websites in other markets for reference:

https://brommelgarage.com/starter-alternator-rebuilding/

https://www.quintonmotorworks.com/auto-repairs/alternator-starter-rebuilds.aspx

https://www.lorvexcharging.com/

https://www.damblingwx.com/

The website can have areas for: services and products offered, high output alternators, Morlin Batteries, troubleshooting tips, current specials, contact info and directions/map, etc. Whatever else you feel applies.

At some point I do want to be able to sell items directly online or at least have a secure section for customers to submit invoice payments, but that's not necessarily in scope for this project just something to keep in mind.

Target Market(s)

Mechanics and Managers in fleet shops, construction and marine industries, shipping trades. Also automobile owners who work on their own vehicles. We sell and rebuild starters and alternators for automobiles, heavy duty equipment, forklifts, gradalls, man movers, bobcats, loaders, large tractors and trucks, just about any engine, golf carts, generators, etc.

Industry/Entity Type

Automotive Part

Coding

Coded - Design and coding required

Number of Pages Required

5+ page

Font styles to use
Serif
Sans Serif

Colors
0255a3
ec1f27
ffffff

Requirements
Must have
• Should also display nicely on mobile phones. Highlight our specialty, "Starters & Alternators"

```html
<!DOCTYPE html>
<html lang="en">
<head>
<meta charset="utf-8">
<title>Kaimana Harbor Rebuilders – Starters &amp; Alternators</title>
<link href="https://fonts.googleapis.com/css2?family=Oswald:wght@300;400;500;600&family=Raleway:wght@400;500;600;700&display=swap" rel="stylesheet">
<style>
:root{
  --blue:#0255a3;
  --blue-dark:#034a8e;
  --red:#ec1f27;
  --white:#ffffff;
  --ink:#555555;
  --text:#5a5a5a;
  --topbar:#4a4a4a;
  --bottombar:#3b3b3b;
  --hero-top:#f2f2f2;
  --hero-bottom:#c9c9c9;
}
*{box-sizing:border-box;margin:0;padding:0}
html,body{width:1200px;height:2341px;overflow:hidden}
body{font-family:"Raleway",sans-serif;color:var(--text);background:var(--white)}
.page{position:relative;width:1200px;height:2341px;overflow:hidden}
.abs{position:absolute}
.btn{position:absolute;background:var(--red);color:var(--white);font:500 10px "Raleway",sans-serif;text-transform:uppercase;display:flex;align-items:center;justify-content:center;letter-spacing:.2px}

/* top bar */
.topbar{left:0;top:0;width:1200px;height:25px;background:var(--topbar);color:var(--white);font-size:9.5px}
.topbar span{position:absolute;top:7px;display:flex;align-items:center;gap:8px}
.topbar svg{width:11px;height:11px;fill:var(--white)}

/* header */
.brand{left:250px;top:44px;font:700 15px "Raleway",sans-serif;color:var(--blue);display:flex;align-items:center;gap:7px;letter-spacing:.3px}
.brand i{width:12px;height:12px;background:var(--red);border-radius:50%;display:block}
.claims{top:40px;display:flex}
.claim{border-left:1px solid var(--blue);padding:0 10px;font-size:9.5px;line-height:12px;color:#444}
.claim:last-child{border-right:1px solid var(--blue)}
.claim b{display:block;font-weight:600}

/* nav */
.nav{left:250px;top:84px;width:702px;height:42px;background:var(--blue);display:flex;align-items:center}
.nav a{color:var(--white);text-decoration:none;font-size:10px;text-transform:uppercase;height:42px;display:flex;align-items:center;padding:0 18px;position:relative}
.nav a+a::before{content:"";position:absolute;left:0;top:16px;height:10px;border-left:1px solid rgba(255,255,255,.5)}
.nav a.active{background:var(--red);padding:0 20px}
.nav a.active+a::before{display:none}
.search{position:absolute;right:26px;top:11px;width:150px;height:20px;border:1px solid var(--white);color:var(--white);font-size:9.5px;padding:4px 8px}
.search svg{position:absolute;right:6px;top:4px;width:11px;height:11px;fill:none;stroke:var(--white);stroke-width:2}

/* hero */
.hero{left:0;top:126px;width:1200px;height:484px;background:linear-gradient(var(--hero-top),#e4e4e4 55%,var(--hero-bottom))}
.hero-photo{left:270px;top:210px;width:325px;height:300px;border-radius:46% 50% 44% 48%;background:radial-gradient(circle at 45% 45%,#f6f6f6,#a8a8a8 55%,#4b4b4b 80%,transparent 81%)}
.hero-title{left:622px;top:192px;font:600 45px/52px "Raleway",sans-serif;color:var(--ink);letter-spacing:1px}
.hero-lead{left:621px;top:368px;width:350px;font:300 13.5px/20px "Oswald",sans-serif;color:#444}

/* feature cards */
.card{top:568px;width:215px;height:212px;background:var(--white);text-align:center}
.card .badge{position:absolute;left:74px;top:-37px;width:66px;height:66px;border-radius:50%;background:var(--red);display:flex;align-items:center;justify-content:center}
.card .badge svg{width:30px;height:30px;fill:none;stroke:var(--white);stroke-width:1.8}
.card h3{margin-top:37px;font:500 16px "Oswald",sans-serif;color:var(--blue)}
.card p{font-size:10.5px;line-height:19px;color:#555;padding:4px 12px 0}

/* services */
.section-title{left:0;width:1200px;text-align:center;font:500 18px "Oswald",sans-serif;color:var(--blue);letter-spacing:.3px}
.section-title::after{content:"";display:block;width:120px;margin:6px auto 0;border-top:1px solid var(--blue)}
.intro{left:345px;top:882px;width:510px;text-align:center;font-size:9px;line-height:12px;color:#555}
.panel{left:250px;top:932px;width:702px;height:224px;box-shadow:0 6px 8px -4px rgba(0,0,0,.35)}
.tabs{left:250px;top:932px;width:151px;height:206px;border:1px solid #c6d4e4;border-top:2px solid var(--blue);border-bottom:2px solid var(--blue);background:var(--white)}
.tab{position:absolute;left:0;width:149px;height:50px;display:flex;align-items:center;gap:10px;padding-left:12px;font-size:10px;color:var(--blue);text-transform:uppercase;line-height:12px}
.tab svg{width:20px;height:20px;fill:none;stroke:var(--blue);stroke-width:1.5;flex:none}
.tab.active{background:var(--blue);color:var(--white)}
.tab.active svg{stroke:var(--white)}
.tab-rule{position:absolute;left:40px;top:152px;width:90px;border-top:1px solid #999}
.engine-photo{top:934px;width:153px;height:92px;border:2px solid var(--blue)}
.panel-text{left:432px;top:1048px;width:520px;font-size:9px;line-height:12px;color:#555}

/* banner */
.banner{left:0;top:1197px;width:1200px;height:366px;background:radial-gradient(ellipse at 30% 30%,#2a6cb0,var(--blue) 45%,var(--blue-dark))}
.battery{left:528px;top:1258px;width:144px;height:116px}
.banner-title{left:0;top:1398px;width:1200px;text-align:center;font:600 29px/36px "Raleway",sans-serif;color:var(--white);letter-spacing:.3px}
.banner-sub{left:0;top:1433px;width:1200px;text-align:center;font:500 13.5px/18px "Oswald",sans-serif;color:var(--white);text-transform:uppercase}

/* troubleshooting */
.drawing{left:250px;top:1677px;width:360px;height:337px;background:radial-gradient(circle at 65% 62%,#e8e8e8,#f7f7f7 45%,var(--white) 70%)}
.tips-intro{left:630px;top:1693px;width:322px;font-size:9px;line-height:12px;color:#555;text-transform:uppercase}
.timeline{left:637px;top:1775px;height:180px;border-left:1px solid var(--blue)}
.tip{left:630px;width:322px}
.tip .num{position:absolute;left:0;top:0;width:16px;height:16px;border:1px solid var(--blue);background:var(--white);font-size:8.5px;color:var(--blue);display:flex;align-items:center;justify-content:center}
.tip h4{position:absolute;left:24px;top:2px;font:600 10px "Raleway",sans-serif;color:var(--blue);text-transform:uppercase}
.tip p{position:absolute;left:26px;top:20px;width:300px;font-size:8.8px;line-height:12px;color:#555}

/* footer */
.footer{left:0;top:2070px;width:1200px;height:243px;background:var(--blue);color:var(--white)}
.map{left:250px;top:2110px;width:213px;height:160px;background:linear-gradient(135deg,#eef0ec,#dfe6dc 50%,#e9ecef)}
.footer-title{top:2106px;font:500 13px "Oswald",sans-serif;text-transform:uppercase;letter-spacing:.3px;color:var(--white)}
.footer-title::after{content:"";display:block;width:68px;margin-top:5px;border-top:1px solid rgba(255,255,255,.7)}
.news{left:508px;width:192px;color:var(--white)}
.news .date{position:absolute;left:0;top:0;width:24px;height:26px;background:var(--white);color:var(--blue);font-size:8px;text-align:center;line-height:11px;padding-top:2px}
.news p{position:absolute;left:37px;top:0;width:160px;font-size:8.5px;line-height:11px}
.news span{position:absolute;left:37px;top:54px;font-size:8.5px}
.news-rule{left:545px;top:2203px;width:154px;border-top:1px solid rgba(255,255,255,.5)}
.contact{left:752px;top:2140px;font-size:10px;line-height:18px;font-weight:600;color:var(--white)}
.contact dt{position:absolute;left:0;width:60px}
.contact dd{position:absolute;left:57px;width:150px}
.social{top:2213px;width:22px;height:22px;border:1px solid var(--white)}
.bottombar{left:0;top:2312px;width:1200px;height:29px;background:var(--bottombar);color:var(--white);font-size:8.5px;font-weight:600}
.bottombar span{position:absolute;top:10px}
</style>
</head>
<body>
<div class="page">

  <!-- top bar -->
  <div class="abs topbar">
    <span style="left:250px"><svg viewBox="0 0 12 12"><circle cx="6" cy="6" r="5.5"/></svg>2730 Makani Lane, Honolulu, HI 96817</span>
    <span style="left:473px"><svg viewBox="0 0 12 12"><path d="M2 1l2.5-.5 1.5 3-1.5 1a7 7 0 003 3l1-1.5 3 1.5-.5 2.5C6 11 1 6 2 1z"/></svg>808-555-0147</span>
    <span style="left:820px">Friendwall</span>
    <span style="left:900px">Chirpline</span>
  </div>

  <!-- header -->
  <div class="abs brand"><i></i>KAIMANA REBUILDERS</div>
  <div class="abs claims" style="left:709px">
    <div class="claim"><b>Leading Provider</b>of alternator</div>
    <div class="claim"><b>Number # 1</b>Rebuilders</div>
    <div class="claim"><b>Certified</b>Starters</div>
  </div>

  <nav class="abs nav">
    <a class="active">Home</a><a>About</a><a>Services</a><a>Products</a><a>Blog</a><a>Contact Us</a>
    <div class="search">Search...<svg viewBox="0 0 12 12"><circle cx="5" cy="5" r="3.5"/><path d="M7.5 7.5L11 11"/></svg></div>
  </nav>

  <!-- hero -->
  <section class="abs hero"></section>
  <div class="abs hero-photo" role="img" aria-label="Product photo of a chrome alternator"></div>
  <h1 class="abs hero-title">REBUILDERS<br>STARTER<br>ALTERNATOR</h1>
  <p class="abs hero-lead">All of our Starters and Alternators are high quality Automotive, Marine, Heavy Duty &amp; shop has been in Honolulu.</p>
  <div class="btn" style="left:622px;top:422px;width:87px;height:26px">Contact Us</div>

  <!-- cards -->
  <article class="abs card" style="left:250px">
    <div class="badge"><svg viewBox="0 0 30 30"><circle cx="13" cy="13" r="8"/><path d="M19 19l7 7"/></svg></div>
    <h3>ABOUT</h3>
    <p>The Starter and Alternator shop has been in Kalihi for close to ten years! Kaimana Harbor Rebuilders is proud to be a small business serving in Kalihi and surrounding areas. With our huge inventory and our great work ethic you won't need to worry about your starter or alternator not working again!</p>
  </article>
  <article class="abs card" style="left:493px">
    <div class="badge"><svg viewBox="0 0 30 30"><rect x="6" y="9" width="18" height="14" rx="2"/><path d="M10 9V6h10v3M11 16h8"/></svg></div>
    <h3>PRODUCTS</h3>
    <p>All of our Starters and Alternators are high quality. We sell Varnek, Holt Crane, Ridley Marsh, Ostrava, Takimura and more! Not only do we sell and re-build automotive Starters and Alternators but also heavy duty, golf cart, marine, ATV, jet ski, lift gate motors and more!</p>
  </article>
  <article class="abs card" style="left:737px">
    <div class="badge"><svg viewBox="0 0 30 30"><circle cx="15" cy="15" r="9"/><circle cx="15" cy="15" r="4"/><path d="M15 3v3M15 24v3M3 15h3M24 15h3"/></svg></div>
    <h3>SERVICES</h3>
    <p>Here at Kaimana Harbor Rebuilders we carry close to one thousand units in stock, or can rebuild your starter or alternator in as little as one to two hours, we can also order in new units as well</p>
  </article>

  <!-- services & products -->
  <h2 class="abs section-title" style="top:838px">SERVICES &amp; PRODUCTS WE OFFERED</h2>
  <p class="abs intro">Do you lack steady voltage or have low-idle output? If you have a large stereo or an off-road vehicle with extra lights and/or a winch, look no further than KAIMANA HARBOR Alternators to supply the power your vehicle deserves.</p>

  <div class="abs panel"></div>
  <div class="abs tabs">
    <div class="tab" style="top:1px"><svg viewBox="0 0 20 20"><rect x="2" y="5" width="16" height="12"/><path d="M11 7l-3 5h4l-3 4"/></svg>Morlin Batteries</div>
    <div class="tab active" style="top:52px"><svg viewBox="0 0 20 20"><rect x="3" y="4" width="14" height="12" rx="3"/><path d="M7 4v12M10 4v12M13 4v12"/></svg>High Output<br>Alternators</div>
    <div class="tab" style="top:102px"><svg viewBox="0 0 20 20"><circle cx="8" cy="8" r="5"/><path d="M12 12l6 6"/></svg>Diagnostics</div>
    <div class="tab-rule"></div>
    <div class="tab" style="top:153px"><svg viewBox="0 0 20 20"><path d="M4 16l8-8M12 8a4 4 0 105-5l-2 2-2-2 2-2"/></svg>Maintenance</div>
  </div>
  <div class="abs engine-photo" role="img" aria-label="Photo of a blue engine bay" style="left:432px;background:linear-gradient(135deg,#2f4f86,#7a8aa3 45%,#c3ccd9 60%,#1c2e55)"></div>
  <div class="abs engine-photo" role="img" aria-label="Photo of a chrome V8 engine" style="left:615px;background:linear-gradient(135deg,#4d5e7a,#9aa7b9 40%,#2c3b57 70%,#6d7d95)"></div>
  <div class="abs engine-photo" role="img" aria-label="Photo of a red and chrome engine" style="left:797px;background:linear-gradient(135deg,#2b2b2e,#8f8f95 40%,#b2262b 65%,#2a2a2e)"></div>
  <p class="abs panel-text">Turn your failing alternator or starter around for less money, or buy a replacement. Talk with our professionals about rebuilding today. Since 1978, we've been helping drivers stay on the road with honest service. Our specialty is in our name. Kealoha's Alternator &amp; Starter is your source for quality work and timely service. We have years of rebuilding experience.</p>
  <div class="btn" style="left:432px;top:1112px;width:86px;height:25px">Contact Us</div>

  <!-- banner -->
  <section class="abs banner" role="img" aria-label="Blue-toned photo of an engine with air filter"></section>
  <svg class="abs battery" viewBox="0 0 144 116" fill="none" stroke="#ffffff" stroke-width="7">
    <rect x="8" y="18" width="128" height="92"/>
    <rect x="24" y="6" width="20" height="12" fill="#ffffff"/>
    <rect x="100" y="6" width="20" height="12" fill="#ffffff"/>
    <path d="M24 34h16M104 34h16M112 26v16" stroke-width="5"/>
    <path d="M78 28L58 70h18l-12 34 28-46H74l12-30z" fill="#ffffff" stroke="none"/>
  </svg>
  <h2 class="abs banner-title">DON'T SETTLE FOR USED PARTS</h2>
  <p class="abs banner-sub">Give your vehicle the best high output power and OEM reliability it deserves</p>
  <div class="btn" style="left:539px;top:1477px;width:123px;height:25px">See Our Alternators</div>

  <!-- troubleshooting -->
  <h2 class="abs section-title" style="top:1618px">TROUBLESHOOTING TIPS</h2>
  <div class="abs drawing" role="img" aria-label="Line drawing of an alternator"></div>
  <p class="abs tips-intro">To successfully do the troubleshooting, it is suggested to always carry your vehicle's repair manual with you. This will help you to identify all the different wires and thus will make the alternator troubleshooting quite easy and convenient.</p>
  <div class="abs timeline"></div>
  <div class="abs tip" style="top:1767px"><div class="num">01</div><h4>Car's Engine</h4><p>Start the car's engine and keep it idle for some time. Also, apply the parking brakes and then set the neutral transmission.</p></div>
  <div class="abs tip" style="top:1818px"><div class="num">02</div><h4>System Load</h4><p>The next thing that you can do is to apply system load by turning on the high beams, AC, wipers along with the other accessories of the car.</p></div>
  <div class="abs tip" style="top:1870px"><div class="num">03</div><h4>Test Leads</h4><p>Make use of your voltmeter test leads and touch both the positive battery post and the B+ terminal connector.</p></div>
  <div class="abs tip" style="top:1922px"><div class="num">04</div><h4>Test Leads</h4><p>Make use of your voltmeter test leads and touch both the positive battery post and the B+ terminal connector.</p></div>
  <div class="btn" style="left:630px;top:1984px;width:87px;height:26px">Read More</div>

  <!-- footer -->
  <footer class="abs footer"></footer>
  <div class="abs map" role="img" aria-label="Street map showing the shop location"></div>
  <h5 class="abs footer-title" style="left:508px">Latest News</h5>
  <div class="abs news" style="top:2134px"><div class="date">04<br>June</div><p>Orci varius natoque penatibus et magnis dis parturient montes, nascetur ridiculus mus. Ut interdum finibus convallis. Pellentesque sit amet dui blandit.</p><span>26 Comments</span></div>
  <div class="abs news-rule"></div>
  <div class="abs news" style="top:2212px"><div class="date">08<br>June</div><p>Orci varius natoque penatibus et magnis dis parturient montes, nascetur ridiculus mus. Ut interdum finibus convallis. Pellentesque sit amet dui blandit.</p><span>0 Comments</span></div>
  <h5 class="abs footer-title" style="left:752px">Get In Touch</h5>
  <dl class="abs contact">
    <dt style="top:0">Address:</dt><dd style="top:0">2730 Makani Lane, Honolulu,<br>HI 96817.</dd>
    <dt style="top:40px">Phone:</dt><dd style="top:40px">808-555-0147</dd>
  </dl>
  <div class="abs social" style="left:752px"></div>
  <div class="abs social" style="left:786px"></div>
  <div class="abs social" style="left:820px"></div>

  <div class="abs bottombar"><span style="left:250px">© Copy Right 2019. All Right Reserved</span></div>
</div>
</body>
</html>
```